CALM.OTTER snowsport and living

Calm Otter webpage design brief

Calm Otter is a life style brand
for those who love winter, snowboarding, and coffee.

We have log houses at some best snowboarding locations in Japan, in which easy and comfortable ambience make guests feel at home during their winter stay. Out there on the slopes, there are Calm Otter’s exclusive coffee kiosks that offer a wide selection of fine coffee from boutique roasters over the world to warm the hands and hearts of whenever our guests need!

Enjoy the snow with Calm Otter!

Tone & Manner: Simple, Tranquil, Relaxed, Enjoyable
 
Look and Feel : Monotone images of log house in the snowy winter and snowboarding people.  Capture of real-people-real-life moments. Red and blue colors can be used on icons and other vector elements in a much smaller scale in the overall picture.  Please refer to the attached color pallette.

Mainly informational with links to Stayvorn for booking
Social media registration pass over from talkloop. pagemural or Stayvorn
Recruitment link to Jobvane

Currently I do not have any pictures. So need a bit of discussion on this area.

Also the website needs to be in 3 languages, English, Chinese and Japanese.

Rough Sitemap:

Home (language selection on every page)
About
GO (snow villas)
Coffee (coffee kiosks on slopes)
Reservations

(Bottom of screen)
Contact us
Company info
Recruit

Reference website:
Quillbrook.example
Mossgate.example.jp

Attached pictures are for references not for use!!!
Color reference pls refer to attached file 4.

Reason: More updates on project briefs. Please have a look.

Target Market(s)

Snowboarders

Industry/Entity Type

Hospitality

Number of Pages Required

5+ page

Font styles to use
Sans Serif

Colors

Designer to choose colors to be used in the design.

Requirements
Must have
• Mobile version
• 3 languages
• Registration thru TalkLoop, Pagemural or Stayvorn
Nice to have
• Illustration instead of pictures

```html
<!DOCTYPE html>
<html lang="en">
<head>
<meta charset="utf-8">
<title>Calm Otter – Snowsport and Living</title>
<link rel="stylesheet" href="https://fonts.googleapis.com/css2?family=Open+Sans:wght@400;600;700;800&family=Ubuntu:wght@400;500&display=swap">
<style>
:root{
  --navy:#2e3347;
  --red:#c8202f;
  --ink:#2b2f3d;
  --muted:#7d8089;
  --line:#eceef0;
  --footer:#e9edef;
  --white:#ffffff;
}
*{margin:0;padding:0;box-sizing:border-box}
html,body{width:772px;height:1200px;overflow:hidden;background:var(--white)}
body{position:relative;font-family:"Open Sans",sans-serif;color:var(--ink)}
a{color:inherit;text-decoration:none}
.abs{position:absolute}

/* brand */
.brand{display:flex;align-items:center;gap:6px;font-family:"Ubuntu",sans-serif;font-weight:400;font-size:19px;line-height:1;white-space:nowrap}
.brand-dot{width:7px;height:7px;border-radius:50%;background:currentColor}
.header-brand{left:110px;top:19px;color:var(--white)}
.footer-brand{left:111px;top:1050px;color:var(--navy)}

/* header */
.site-header{left:0;top:0;width:772px;height:57px;background:var(--navy)}
.main-nav a{position:absolute;top:22px;font-size:7.6px;font-weight:600;color:var(--white);white-space:nowrap}
.social{display:flex;gap:4px}
.social span{display:block;width:19px;height:19px;border:1px solid rgba(255,255,255,.75);border-radius:50%}
.header-social{left:556px;top:19px}
.footer-social{left:111px;top:1090px}
.footer-social span{border-color:#9aa0a8}
.lang{left:633px;top:23px;font-size:7.6px;font-weight:700;color:var(--white);display:flex;align-items:center;gap:3px}

/* hero */
.hero{left:0;top:57px;width:772px;height:289px;background:
  radial-gradient(ellipse 190px 110px at 360px 190px,rgba(70,78,92,.55),rgba(70,78,92,0) 100%),
  linear-gradient(180deg,#b9c1c8 0%,#a7b0b9 40%,#d9dee2 72%,#f1f3f5 100%)}
.hero-title{left:0;top:170px;width:772px;text-align:center;font-weight:800;font-size:28px;line-height:29px;color:var(--navy);letter-spacing:0.3px}
.hero-title em{display:block;font-style:normal;color:var(--red)}

/* welcome */
.welcome-photo{left:111px;top:375px;width:268px;height:164px;background:linear-gradient(135deg,#c4cbd2,#8d98a3 55%,#a9b2ba);border:4px solid #dfe3e6}
.welcome{left:405px;top:381px;width:244px;text-align:center}
.eyebrow{font-size:8.4px;font-weight:600;color:var(--ink)}
.section-title{font-family:"Ubuntu",sans-serif;font-weight:400;font-size:15px;color:var(--ink)}
.welcome .section-title{margin-top:3px}
.body-copy{font-size:7.6px;line-height:13.5px;color:var(--muted)}
.welcome .body-copy{margin-top:7px}
.btn{display:inline-block;height:19px;line-height:17px;padding:0 13px;border-radius:10px;font-size:7.6px;font-weight:600;border:1px solid}
.btn-outline{border-color:#6f7480;color:var(--ink)}
.welcome .btn{margin-top:11px}

.divider{left:0;width:772px;height:1px;background:var(--line)}

/* villas */
.villas-title{left:0;top:593px;width:772px;text-align:center}
.villa{top:628px;width:174px;height:173px}
.villa-1{left:118px;background:linear-gradient(180deg,#d3d9de 0%,#aeb7bf 35%,#7f8a95 65%,#e3e7ea 100%)}
.villa-2{left:299px;background:linear-gradient(180deg,#5f6975 0%,#7c8691 45%,#9aa3ad 70%,#c6ccd2 100%)}
.villa-3{left:480px;background:linear-gradient(180deg,#dfe4e8 0%,#a3adb6 35%,#7a8590 70%,#c9cfd4 100%)}
.arrow{top:708px}

/* feature cards */
.card{top:859px;width:268px;height:130px;color:var(--white)}
.card-recruit{left:111px;background:var(--navy)}
.card-coffee{left:393px;background:var(--red)}
.card-icon{position:absolute;left:14px;top:15px}
.card-body{position:absolute;left:61px;top:10px;width:188px}
.card-title{font-family:"Ubuntu",sans-serif;font-weight:500;font-size:15px;line-height:20px}
.card .body-copy{color:rgba(255,255,255,.78);margin-top:4px}
.btn-light{border-color:var(--white);color:var(--white);margin-top:8px;display:inline-flex;align-items:center;gap:5px}

/* footer */
.site-footer{left:0;top:1019px;width:772px;height:181px;background:var(--footer)}
.footer-heading{font-size:8.4px;font-weight:600;color:var(--ink)}
.footer-list{margin-top:6px;font-size:7.6px;line-height:13.6px;color:var(--muted);list-style:none}
.contact{left:252px;top:1046px}
.contact .phone{color:var(--red);font-weight:600;font-size:8.4px;margin-top:5px;line-height:14px}
.quick{left:423px;top:1046px}
.newsletter{left:534px;top:1046px;width:127px}
.email-field{margin-top:8px;height:20px;border-radius:10px;background:var(--white);font-size:7.6px;color:#aab0b6;padding:0 11px;line-height:20px}
.subscribe{margin-top:5px;height:19px;border-radius:10px;background:var(--navy);color:var(--white);font-size:7.6px;font-weight:600;padding:0 4px 0 12px;display:flex;align-items:center;justify-content:space-between}
.subscribe i{width:12px;height:12px;border-radius:50%;background:var(--white);display:flex;align-items:center;justify-content:center}
.copyright{left:111px;top:1165px;font-size:7.6px;color:var(--muted)}
.legal{right:111px;top:1165px;font-size:7.6px;color:var(--muted)}
.legal span{margin:0 4px}
</style>
</head>
<body>

<header class="site-header abs">
  <a class="brand header-brand abs" href="#"><span>Calm Otter</span><i class="brand-dot"></i></a>
  <nav class="main-nav abs" style="left:309px;top:0">
    <a href="#" style="left:0">Home</a>
    <a href="#" style="left:39px">About</a>
    <a href="#" style="left:80px">Snow Villas</a>
    <a href="#" style="left:138px">Coffee</a>
    <a href="#" style="left:180px">Reservations</a>
  </nav>
  <div class="social header-social abs">
    <span aria-label="Pagemural"></span>
    <span aria-label="TalkLoop"></span>
    <span aria-label="Stayvorn"></span>
  </div>
  <div class="lang abs">
    <svg width="8" height="8" viewBox="0 0 10 10" fill="none" stroke="#fff" stroke-width="0.9"><circle cx="5" cy="5" r="4.2"/><ellipse cx="5" cy="5" rx="1.8" ry="4.2"/><line x1="0.8" y1="5" x2="9.2" y2="5"/></svg>
    EN
    <svg width="5" height="4" viewBox="0 0 5 4"><path d="M0 0.5h5L2.5 3.5z" fill="#fff"/></svg>
  </div>
</header>

<section class="hero abs" role="img" aria-label="Monotone photo of a snow-covered log house among frosted trees"></section>
<h1 class="hero-title abs">ENJOY THE SNOW WITH <em>CALM OTTER</em></h1>

<div class="welcome-photo abs" role="img" aria-label="Monotone photo of a log house living room with fireplace"></div>
<section class="welcome abs">
  <p class="eyebrow">Welcome to</p>
  <h2 class="section-title">Calm Otter Snowsport and Living</h2>
  <p class="body-copy">Nam nec tellus a odio tincidunt auctor a ornare odio. Sed non sociosqu ad litora torquent per conubia nostra, per inceptos himenaeos. Mauris in erat justo. Nullam ac urna eu felis dapibus condimentum sit amet a augue. Sed non neque elit. Sed ut imperdiet nisi. Proin &nbsp;fermentum nunc. Etiam pharetra, erat sed nisl quis neque. Suspendisse in orci enim.</p>
  <a class="btn btn-outline" href="#">Learn More</a>
</section>

<div class="divider abs" style="top:568px"></div>

<h2 class="section-title villas-title abs">Snow Villas</h2>
<svg class="arrow abs" style="left:103px" width="9" height="9" viewBox="0 0 9 9" fill="none" stroke="#8a8f98" stroke-width="0.9"><path d="M8 4.5H1M4 1.5L1 4.5l3 3"/></svg>
<div class="villa villa-1 abs" role="img" aria-label="Monotone photo of a log chalet among pine trees below snowy peaks"></div>
<div class="villa villa-2 abs" role="img" aria-label="Monotone photo of a modern villa under a starry night sky"></div>
<div class="villa villa-3 abs" role="img" aria-label="Monotone photo of a large timber lodge in the snow"></div>
<svg class="arrow abs" style="left:660px" width="9" height="9" viewBox="0 0 9 9" fill="none" stroke="#8a8f98" stroke-width="0.9"><path d="M1 4.5h7M5 1.5l3 3-3 3"/></svg>

<div class="divider abs" style="top:830px"></div>

<section class="card card-recruit abs">
  <svg class="card-icon" width="30" height="32" viewBox="0 0 30 32" fill="none" stroke="#fff" stroke-width="1.1">
    <rect x="3" y="12" width="16" height="17" rx="3"/>
    <path d="M5 12c0-5 2.5-8 6-8s6 3 6 8"/>
    <line x1="5" y1="17" x2="17" y2="17"/><line x1="5" y1="21" x2="17" y2="21"/>
    <rect x="21" y="3" width="3" height="26" rx="1.5"/><rect x="25" y="3" width="3" height="26" rx="1.5"/>
  </svg>
  <div class="card-body">
    <h3 class="card-title">Recruitment</h3>
    <p class="body-copy">Nullam ac urna eu felis dapibus condimentum sit amet a augue. Sed non neque elit. Sed ut imperdiet nisi. Proin &nbsp;fermentum nunc. Etiam pharetra, erat sed nisl quis neque. Suspendisse in orci enim.</p>
    <a class="btn btn-light" href="#"><svg width="8" height="8" viewBox="0 0 8 8"><rect width="8" height="8" rx="1.5" fill="#fff"/></svg>Jobvane</a>
  </div>
</section>

<section class="card card-coffee abs">
  <svg class="card-icon" width="30" height="32" viewBox="0 0 30 32" fill="none" stroke="#fff" stroke-width="1.1">
    <path d="M9 3c-2 2 2 3 0 6M14 3c-2 2 2 3 0 6M19 3c-2 2 2 3 0 6"/>
    <path d="M4 13h20v5a8 8 0 0 1-8 8h-4a8 8 0 0 1-8-8z"/>
    <path d="M24 15h2a3 3 0 0 1 0 6h-2.5"/>
    <line x1="2" y1="29" x2="28" y2="29"/>
  </svg>
  <div class="card-body">
    <h3 class="card-title">Coffee kiosks on slopes</h3>
    <p class="body-copy">Nullam ac urna eu felis dapibus condimentum sit amet a augue. Sed non neque elit. Sed ut imperdiet nisi. Proin &nbsp;fermentum nunc. Etiam pharetra, erat sed nisl quis neque. Suspendisse in orci enim.</p>
    <a class="btn btn-light" href="#">Learn More</a>
  </div>
</section>

<footer class="site-footer abs"></footer>
<a class="brand footer-brand abs" href="#"><span>Calm Otter</span><i class="brand-dot"></i></a>
<div class="social footer-social abs">
  <span aria-label="Pagemural"></span>
  <span aria-label="TalkLoop"></span>
  <span aria-label="Stayvorn"></span>
</div>

<div class="contact abs">
  <h4 class="footer-heading">Contact Information</h4>
  <ul class="footer-list">
    <li>Calm Otter Snowsport and Living</li>
    <li>228, Lorem ipsum dolor Sit</li>
    <li>Dosis amet sit - 54985</li>
  </ul>
  <p class="phone">1800 555 0142</p>
  <p class="footer-list" style="margin-top:0">info@calmotter.example</p>
</div>

<div class="quick abs">
  <h4 class="footer-heading">Quick Links</h4>
  <ul class="footer-list">
    <li>Home</li><li>About</li><li>Snow Villas</li><li>Coffee</li><li>Reservations</li>
  </ul>
</div>

<div class="newsletter abs">
  <h4 class="footer-heading">Newsletter</h4>
  <div class="email-field">Email Address</div>
  <div class="subscribe">Subscribe <i><svg width="5" height="6" viewBox="0 0 5 6" fill="none" stroke="#2e3347" stroke-width="1.2"><path d="M1 0.8L3.5 3 1 5.2"/></svg></i></div>
</div>

<p class="copyright abs">Copyright © 2017 Calm Otter Snowsport and Living.</p>
<p class="legal abs">Terms of Use<span>|</span>Privacy Policy<span>|</span>Sitemap</p>

</body>
</html>
```